NOTE: I PROVIDED THE INCORRECT LOGO AND ONLY A HANDFUL OF PEOPLE NOTICED THAT IT WAS NOT THE ONE I DESCRIBED. THE LOGO I HAVE NOW ATTACHED MATCHES MY WEBSITE AND THE COLORS ON THE WEBSITE SHOULD BE USED FOR THE CARD.

PLEASE READ THE BUSINESS CARD DETAILS AND PROJECT MUST HAVES CAREFULLY.

I am looking for a business card that is powerful, a bit edgy, and although I work in the corporate world, not too formal. I would like to see designs that use the colors on my website www.brightlumo.com. I don't want the card to look washed out so please use shades of those colors that make them "pop". The "vibe" of the card needs to show substance and confidence while also reflecting that we're not your usual consultants.

The focus of my work is turning "people problems" into profits. Those problems could be poor service, an unstable workforce, untrained leaders, or managing change. We are an aggressive, results-focused team of performance improvement professionals who refuse to believe "things can't be done". For us, failure is not an option. Our logo reflects a target from the view of the site on a gun.

In addition to the contact information provided on the sample business card (do not include "turning people problems into profits"), I would like to include this statement (probably on the back):
I equip results-oriented business leaders to turn their people problems into profits in six months or less.

PLEASE NOTE THAT MY WEBSITE IS UNDER REVISION TO TONE DOWN THE MILITARY THEME, ALTHOUGH THE WARRIOR ENERGY AND FOCUS ON RESULTS REMAINS.

Target Market(s)

My clients are Mid and senior-level managers. I don't target any particular industry.

Industry/Entity Type

Consulting

Contact Information for Business Card

In addition to the contact information provided on the sample business card (DO NOT INCLUDE "turning people problems into profits"), I would like to include this statement (probably on the back):

I don't care whether the card is landscape or portrait view.

Font styles to use
Sans Serif

Requirements
Must have
• 1. be easy to read, no 6-8 point fonts!
• 2. a "vibe" that captures the eye without being too chaotic or busy
• 3. bold color, not washed out or boring - a good blend with the colors currently on my website (black, red, white, army green) but you don't need to use all of them.
• 4. all the contact information I have provided
• 5. a good blend with the colors currently on my website
• 6. Must have this quote on the back of the card: I equip results-oriented business leaders to turn their people problems into profits in six months or less.
Nice to have
• In looking at the sample images I provided for ideas, you can see that I like the way a card carries over from one side to the next.
• It would be great to find some aspect/quality/feature that I haven't seen before
Should not have
• 1. NO use of ALL CAPS
• 2. fonts that I would have to seek out and purchase (you should provide files for font if using something not standard)

```html
<!DOCTYPE html>
<html lang="en">
<head>
<meta charset="utf-8">
<title>Bright Lumo — Business Card</title>
<link rel="stylesheet" href="https://fonts.googleapis.com/css2?family=Russo+One&family=Work+Sans:wght@500;600;700&display=swap">
<style>
  :root {
    --page: #161616;
    --card-top: #2b2b2b;
    --card-bottom: #1d1d1d;
    --red: #ee3a2c;
    --silver: #b9b9b9;
    --silver-dim: #8e8e8e;
    --rule: #4a4a4a;
  }
  * { box-sizing: border-box; margin: 0; padding: 0; }
  html, body {
    width: 1200px; height: 900px; overflow: hidden;
    background: var(--page);
    font-family: "Work Sans", sans-serif;
  }
  .stage {
    width: 1200px; height: 900px;
    display: flex; flex-direction: column;
    align-items: center; justify-content: center;
    gap: 44px;
  }
  .card {
    position: relative;
    width: 640px; height: 366px;
    background: linear-gradient(160deg, var(--card-top), var(--card-bottom));
    border-bottom: 7px solid var(--red);
    box-shadow: 0 14px 30px rgba(0,0,0,.55);
    overflow: hidden;
  }
  .brand {
    display: flex; align-items: center; gap: 14px;
  }
  .brand-dot {
    width: 22px; height: 22px; border-radius: 50%;
    background: var(--red);
    flex: none;
  }
  .brand-name {
    font-family: "Work Sans", sans-serif;
    font-weight: 700;
    color: var(--silver);
    line-height: 1;
  }

  /* Back side */
  .card-back {
    display: flex; flex-direction: column;
    align-items: center; justify-content: center;
    padding: 0 60px;
  }
  .card-back .brand-name { font-size: 50px; }
  .mission {
    margin-top: 34px;
    text-align: center;
    font-size: 19px; font-weight: 600;
    line-height: 1.4;
    color: var(--silver-dim);
  }

  /* Front side */
  .card-front {
    display: grid;
    grid-template-columns: 1fr 1px 1.15fr;
    align-items: center;
    padding: 0 36px 0 44px;
  }
  .card-front .brand-name { font-size: 32px; }
  .divider {
    width: 1px; height: 170px; background: var(--rule);
  }
  .details { padding-left: 32px; }
  .person-name {
    font-family: "Russo One", sans-serif;
    font-size: 33px; color: var(--red);
    line-height: 1.05;
  }
  .person-role {
    margin-top: 6px;
    font-size: 17px; font-weight: 600;
    color: var(--silver);
  }
  .contact-list {
    list-style: none;
    margin-top: 22px;
    display: flex; flex-direction: column; gap: 7px;
  }
  .contact-item {
    display: flex; align-items: center; gap: 14px;
    font-size: 18px; font-weight: 600;
    color: var(--silver);
    letter-spacing: .02em;
  }
  .contact-icon { width: 15px; height: 15px; flex: none; }
</style>
</head>
<body>
<main class="stage">

  <section class="card card-back" aria-label="Card back">
    <div class="brand">
      <span class="brand-dot"></span>
      <span class="brand-name">Bright Lumo</span>
    </div>
    <p class="mission">I equip results-oriented business leaders to turn their people problems into profits in six months or less.</p>
  </section>

  <section class="card card-front" aria-label="Card front">
    <div class="brand">
      <span class="brand-dot"></span>
      <span class="brand-name">Bright Lumo</span>
    </div>
    <span class="divider"></span>
    <div class="details">
      <h1 class="person-name">Dana Mercer</h1>
      <p class="person-role">Chief Performance Strategist</p>
      <ul class="contact-list">
        <li class="contact-item">
          <svg class="contact-icon" viewBox="0 0 16 16" aria-hidden="true"><path d="M3 1.5l2.5 0 1.2 3.2-1.6 1.1a8 8 0 0 0 5.1 5.1l1.1-1.6 3.2 1.2v2.5c0 .6-.5 1-1.1 1A12.5 12.5 0 0 1 2 2.6c0-.6.4-1.1 1-1.1z" fill="none" stroke="#ee3a2c" stroke-width="1.5"/></svg>
          555-014-2290
        </li>
        <li class="contact-item">
          <svg class="contact-icon" viewBox="0 0 16 16" aria-hidden="true"><rect x="4" y="1" width="8" height="14" rx="1.5" fill="none" stroke="#ee3a2c" stroke-width="1.5"/><line x1="7" y1="12.3" x2="9" y2="12.3" stroke="#ee3a2c" stroke-width="1.5"/></svg>
          555-017-4381
        </li>
        <li class="contact-item">
          <svg class="contact-icon" viewBox="0 0 16 16" aria-hidden="true"><rect x="1.5" y="3.5" width="13" height="9" rx="1" fill="none" stroke="#ee3a2c" stroke-width="1.5"/><path d="M2 4l6 5 6-5" fill="none" stroke="#ee3a2c" stroke-width="1.5"/></svg>
          danam@brightlumo.com
        </li>
        <li class="contact-item">
          <svg class="contact-icon" viewBox="0 0 16 16" aria-hidden="true"><circle cx="8" cy="8" r="6.5" fill="none" stroke="#ee3a2c" stroke-width="1.4"/><ellipse cx="8" cy="8" rx="2.8" ry="6.5" fill="none" stroke="#ee3a2c" stroke-width="1.2"/><line x1="1.5" y1="8" x2="14.5" y2="8" stroke="#ee3a2c" stroke-width="1.2"/></svg>
          www.brightlumo.com
        </li>
      </ul>
    </div>
  </section>

</main>
</body>
</html>
```